social interest sharing site needs a web site design

we need a web site design for a social web platform.
the site is one page(main page), that is split into 3 sections
each section is a different color(red,green and blue)
and a user can choose to share each of the sections.
any section/color will contain boxes , each box can contain different media types.

the media types:
* list of URLS
* list of articles including title + image + description
* list of videos
* thumbnails of images
* calender
* list of emails

the main content will look like corkboardly layout
multiple boxes each box can contain different type of content as described above

each color is a different tab
each tab will have layout like corkboardly
Updates

please read the last description update.
and i uploaded an image that can explain the requirements better

thanks
Oren
 

Industry/Entity Type

Media

```html
<!DOCTYPE html>
<html lang="en">
<head>
<meta charset="utf-8">
<title>Hueboard – My Home Page</title>
<link href="https://fonts.googleapis.com/css2?family=Open+Sans:wght@400;600;700;800&display=swap" rel="stylesheet">
<style>
:root{
  --red:#fd7672;
  --green:#3ccbb0;
  --blue:#5ba4e0;
  --navy:#0b3d78;
  --sky:#1da1f2;
  --dark:#333333;
  --slate:#45597c;
  --page:#ececec;
  --ink:#444;
  --muted:#777;
}
*{box-sizing:border-box;margin:0;padding:0}
html,body{width:1200px;height:1200px;overflow:hidden}
body{position:relative;background:var(--page);font-family:"Open Sans",Arial,sans-serif;color:var(--ink)}
.topbar{position:absolute;left:0;top:0;width:1200px;height:113px;background:var(--dark)}
.subbar{position:absolute;left:0;top:113px;width:1200px;height:51px;background:#e4e4e4;
  background-image:radial-gradient(#d2d2d2 1px,transparent 1px);background-size:4px 4px}
.brand{position:absolute;left:88px;top:0;width:273px;height:164px;display:flex}
.brand span{flex:1}
.brand .r{background:var(--red)}.brand .g{background:var(--green)}.brand .b{background:var(--blue)}
.brand-name{position:absolute;left:0;top:58px;width:273px;text-align:center;color:#fff;font-weight:800;font-size:38px;letter-spacing:-1px}
.social{position:absolute;top:56px;width:47px;height:47px;border-radius:6px;display:flex;align-items:center;justify-content:center;color:#fff;font-weight:800;font-size:32px}
.login{position:absolute;left:975px;top:74px;color:#fff;font-weight:700;font-size:13px}
.signup{position:absolute;left:1034px;top:64px;width:77px;height:32px;background:var(--red);border-radius:3px;color:#fff;font-weight:700;font-size:12px;display:flex;align-items:center;justify-content:center}
.following{position:absolute;left:374px;top:124px;width:90px;text-align:center;font-weight:700;font-size:12px;line-height:15px;color:#222}
.tab{position:absolute;top:122px;height:33px;background:var(--slate);color:#fff;font-weight:700;font-size:12px;line-height:12px;text-align:center;display:flex;align-items:center;justify-content:center;box-shadow:0 1px 2px rgba(0,0,0,.3)}
.profile{position:absolute;left:88px;top:178px;width:351px;height:99px;background:var(--red);border-radius:0 5px 5px 0;overflow:hidden;color:#fff}
.profile .s1{position:absolute;left:0;top:0;width:22px;height:99px;background:var(--green)}
.profile .s2{position:absolute;left:22px;top:0;width:23px;height:99px;background:var(--blue)}
.profile h1{position:absolute;left:90px;top:7px;font-size:29px;font-weight:700}
.profile .handle{position:absolute;left:93px;top:40px;font-size:17px;font-weight:700}
.profile .stat{position:absolute;top:65px;font-size:12px;font-weight:700;line-height:14px}
.profile .divider{position:absolute;left:123px;top:66px;width:1px;height:27px;background:rgba(255,255,255,.6)}
.gear{position:absolute;right:0;bottom:0;width:38px;height:37px;background:#222;display:flex;align-items:center;justify-content:center}
.card{position:absolute;background:#fff;box-shadow:0 2px 3px rgba(0,0,0,.25);overflow:hidden}
.media{position:absolute;left:0;top:0;width:100%}
.caption{position:absolute;left:0;width:100%;color:#fff;font-size:10.5px;line-height:12px;padding:10px 13px}
.caption.center{text-align:center;font-weight:600}
.c-red{background:var(--red)}.c-green{background:var(--green)}.c-blue{background:var(--blue)}
.share{position:absolute;left:0;top:0;display:flex;z-index:2}
.share i{width:21px;height:21px;display:flex;align-items:center;justify-content:center;color:#fff;font-style:normal;font-weight:800;font-size:14px}
.share .n{background:var(--navy)}.share .t{background:var(--sky)}.share .q,.share .z{background:var(--red)}
.note{padding:0}
.note h3{position:absolute;left:52px;top:20px;font-size:12px;font-weight:400;color:#333}
.note .doc{position:absolute;left:14px;top:14px;width:28px;height:28px;background:#f5c518;border-radius:2px}
.note .doc::after{content:"";position:absolute;left:5px;top:12px;width:18px;height:3px;background:#fff;box-shadow:0 6px 0 #fff}
.note p{position:absolute;left:13px;top:51px;right:30px;font-size:9px;line-height:11.5px;color:#666}
.note .meta{position:absolute;left:12px;bottom:12px;display:flex;align-items:center;gap:6px;font-size:9px;color:#666}
.heart{width:12px;height:11px;background:#ccc;border-radius:6px 6px 2px 2px}
.pin{width:15px;height:15px;background:#d9333f;margin-left:8px}
.spinner{position:absolute;left:576px;top:1037px}
.footer{position:absolute;left:0;top:1125px;width:1200px;height:75px;background:#f7f7f7;border-top:1px solid #dcdcdc}
.footer-brand{position:absolute;left:0;top:30px;width:1200px;display:flex;justify-content:center;align-items:center;gap:8px;font-weight:700;font-size:15px;color:var(--blue)}
.footer-brand span.dot{width:16px;height:16px;border-radius:50%;background:var(--red)}
</style>
</head>
<body>

<header>
  <div class="topbar"></div>
  <div class="subbar"></div>
  <div class="brand"><span class="r"></span><span class="g"></span><span class="b"></span>
    <div class="brand-name">Hueboard.me</div>
  </div>
  <div class="social" style="left:602px;background:var(--navy)" aria-label="Share on social network 1"></div>
  <div class="social" style="left:665px;background:var(--sky)" aria-label="Share on social network 2"></div>
  <div class="social" style="left:728px;background:var(--red)">?</div>
  <div class="social" style="left:791px;background:var(--red)">
    <svg width="28" height="28" viewBox="0 0 28 28"><circle cx="11" cy="11" r="8" fill="none" stroke="#fff" stroke-width="4"/><line x1="17" y1="17" x2="25" y2="25" stroke="#fff" stroke-width="5" stroke-linecap="round"/></svg>
  </div>
  <div class="login">LOGIN</div>
  <div class="signup">SIGN UP</div>
  <nav>
    <div class="following">FOLLOWING<br>HUEBOARD</div>
    <div class="tab" style="left:467px;width:139px">Talis favorites<br>Videos</div>
    <div class="tab" style="left:617px;width:138px">Mayas pic +<br>favorites links</div>
    <div class="tab" style="left:769px;width:138px">Faimiliy weekly<br>calendar and notes</div>
  </nav>
</header>

<section class="profile">
  <div class="s1"></div><div class="s2"></div>
  <h1>MY HOME PAGE</h1>
  <div class="handle">@orensch</div>
  <div class="stat" style="left:52px">142<br>Followers</div>
  <div class="divider"></div>
  <div class="stat" style="left:136px">52<br>Likes</div>
  <div class="gear">
    <svg width="26" height="26" viewBox="0 0 26 26"><circle cx="13" cy="13" r="8" fill="none" stroke="#fff" stroke-width="3" stroke-dasharray="3 2.3"/><circle cx="13" cy="13" r="5" fill="none" stroke="#fff" stroke-width="2"/><line x1="15" y1="15" x2="23" y2="23" stroke="#fff" stroke-width="3"/></svg>
  </div>
</section>

<main>
  <!-- column 1 -->
  <article class="card" style="left:94px;top:307px;width:188px;height:675px">
    <div class="share"><i class="n"></i><i class="t"></i><i class="q">?</i><i class="z">⌕</i></div>
    <div class="media" role="img" aria-label="Photo of a woman in a white blouse and navy skirt in autumn light" style="height:611px;background:linear-gradient(160deg,#c9a36a,#8a6b45 40%,#c08a5a 70%,#ddd)"></div>
    <div class="caption c-green" style="top:611px;height:64px;padding-top:13px">Puffed rose fabric hair bow for little girls with seed pearl wrapper. So elegant, only $1.75!</div>
  </article>

  <!-- column 2 -->
  <article class="card" style="left:296px;top:307px;width:194px;height:195px">
    <div class="share"><i class="n"></i><i class="t"></i><i class="q">?</i><i class="z">⌕</i></div>
    <div class="media" role="img" aria-label="Colored pencils arranged in a circle" style="height:147px;background:radial-gradient(circle,#fff 25%,#f6d13c 45%,#d64ec8 75%,#7d54d8)"></div>
    <div class="caption c-red center" style="top:147px;height:48px;padding-top:14px">Earth vs Middle Earth</div>
  </article>
  <article class="card" style="left:296px;top:518px;width:194px;height:98px">
    <div class="share"><i class="n"></i><i class="t"></i><i class="q">?</i><i class="z">⌕</i></div>
    <div class="media" role="img" aria-label="Dark blue video thumbnail" style="height:98px;background:radial-gradient(circle at 55% 50%,#1d3d5c,#06111f)"></div>
    <svg style="position:absolute;left:62px;top:18px" width="66" height="66" viewBox="0 0 66 66"><circle cx="28" cy="28" r="20" fill="none" stroke="rgba(255,255,255,.6)" stroke-width="6"/><line x1="42" y1="42" x2="58" y2="58" stroke="rgba(255,255,255,.6)" stroke-width="8" stroke-linecap="round"/><path d="M28 18v20M18 28h20" stroke="rgba(255,255,255,.6)" stroke-width="6"/></svg>
  </article>
  <article class="card" style="left:296px;top:626px;width:194px;height:195px">
    <div class="media" role="img" aria-label="Face painted in neon ultraviolet colors" style="height:124px;background:linear-gradient(135deg,#2b7f3f,#6a2a8f 50%,#1a1a2a)"></div>
    <div class="caption c-red" style="top:124px;height:71px;padding-top:16px">love the combo of pottery and drawing!</div>
  </article>

  <!-- column 3 -->
  <article class="card" style="left:506px;top:307px;width:188px;height:309px">
    <div class="share"><i class="n"></i><i class="t"></i><i class="q">?</i><i class="z">⌕</i></div>
    <div class="media" role="img" aria-label="Flower petals floating above a glass bowl" style="height:199px;background:linear-gradient(180deg,#f2f2f2,#cfcfcf 60%,#2a2a2a)"></div>
    <div class="caption c-blue" style="top:199px;height:110px;font-size:9.5px;line-height:11.5px">dicas para concursosApós alguns emails e dicas de usuários, temos um presente de Natal adiantado. StudyNest terá agora uma coluna especial.</div>
  </article>
  <article class="card" style="left:506px;top:627px;width:188px;height:195px">
    <div class="share"><i class="n"></i><i class="t"></i><i class="q">?</i><i class="z">⌕</i></div>
    <div class="media" role="img" aria-label="Flower petals floating above a glass bowl" style="height:137px;background:linear-gradient(180deg,#f2f2f2,#cfcfcf 70%,#2a2a2a)"></div>
    <div class="caption c-green" style="top:137px;height:58px;padding:10px 10px 0 40px;font-size:9px;line-height:12px">Do this workout 3-4 days a week for quicktransformation.</div>
    <div style="position:absolute;left:10px;top:147px;width:22px;height:22px;background:#555;border:1px solid #fff"></div>
  </article>

  <!-- column 4 -->
  <article class="card" style="left:710px;top:307px;width:193px;height:195px">
    <div class="share"><i class="n"></i><i class="t"></i><i class="q">?</i><i class="z">⌕</i></div>
    <div class="media" role="img" aria-label="Cartoon blue bird sitting on a branch" style="height:139px;background:radial-gradient(circle at 50% 40%,#3aa7ea 0 25%,#f4f4f4 26%)"></div>
    <div class="caption c-red" style="top:139px;height:56px;padding-top:15px">Do this workout 3-4 days a week for quick transformation.</div>
  </article>
  <article class="card" style="left:710px;top:518px;width:193px;height:97px">
    <div class="media" role="img" aria-label="Toucan illustration on a night sky" style="height:97px;background:radial-gradient(circle at 50% 50%,#2a6bbd,#0a2357)"></div>
  </article>
  <article class="card" style="left:710px;top:630px;width:193px;height:194px">
    <div class="share"><i class="n"></i><i class="t"></i><i class="q">?</i><i class="z">⌕</i></div>
    <div class="media" role="img" aria-label="Colorful paint splash around a white circle" style="height:134px;background:radial-gradient(circle at 50% 75%,#fff 30%,#f3c04a 45%,#e44c3a 55%,#fff 70%)"></div>
    <div class="caption c-green" style="top:134px;height:60px;padding-top:8px;font-size:10px">Puffed rose fabric hair bow for little girls with seed pearl wrapper. So elegant, only $1.75!</div>
  </article>

  <!-- column 5 -->
  <article class="card" style="left:919px;top:307px;width:189px;height:517px">
    <div class="share"><i class="n"></i><i class="t"></i><i class="q">?</i><i class="z">⌕</i></div>
    <div class="media" role="img" aria-label="Photo of an outfit with yellow blazer and white shorts on stone steps" style="height:469px;background:linear-gradient(180deg,#4a5a3a,#d8c540 25%,#c8b9a6 55%,#8f8275)"></div>
    <div class="caption c-blue center" style="top:469px;height:48px;padding-top:16px;font-size:12px">Fall outfit. #Yellow</div>
  </article>

  <!-- bottom row -->
  <article class="card note" style="left:294px;top:838px;width:306px;height:144px">
    <div class="doc"></div>
    <h3>dicas para concursosApós alguns emails</h3>
    <p>dicas para concursosApós alguns emails e dicas de usuários, temos um presente de Natal adiantado. StudyNest terá agora uma coluna especial dedicada a Concursos Públicos, onde traremos respostas e dicas de estudo para todos que estiverem pensando na carreira de concurseiro.</p>
    <div class="meta"><span class="heart"></span>1<span class="pin"></span></div>
  </article>
  <article class="card note" style="left:618px;top:838px;width:286px;height:144px">
    <div class="doc"></div>
    <h3 style="left:48px">dicas para concursosApós alguns emails</h3>
    <p style="right:14px">dicas para concursosApós alguns emails e dicas de usuários, temos um presente de Natal adiantado. StudyNest terá agora uma coluna especial dedicada a Concursos Públicos, onde traremos respostas e dicas de estudo para todos que estiverem pensando na carreira de concurseiro.</p>
    <div class="meta"><span class="heart"></span>1<span class="pin"></span></div>
  </article>
  <article class="card" style="left:919px;top:838px;width:193px;height:144px">
    <div class="share"><i class="n"></i><i class="t"></i><i class="q">?</i><i class="z">⌕</i></div>
    <div class="media" role="img" aria-label="Animated martial arts character video thumbnail" style="height:144px;background:radial-gradient(circle at 50% 40%,#8a2a1a,#3a0e08)"></div>
    <svg style="position:absolute;left:65px;top:38px" width="66" height="66" viewBox="0 0 66 66"><circle cx="28" cy="28" r="20" fill="none" stroke="rgba(255,255,255,.6)" stroke-width="6"/><line x1="42" y1="42" x2="58" y2="58" stroke="rgba(255,255,255,.6)" stroke-width="8" stroke-linecap="round"/><path d="M28 18v20M18 28h20" stroke="rgba(255,255,255,.6)" stroke-width="6"/></svg>
  </article>
</main>

<svg class="spinner" width="46" height="46" viewBox="0 0 46 46" aria-label="Loading">
  <g stroke-width="2.5" stroke-linecap="round">
    <line x1="23" y1="3" x2="23" y2="13" stroke="#222"/>
    <line x1="37" y1="9" x2="31" y2="15" stroke="#bbb"/>
    <line x1="43" y1="23" x2="33" y2="23" stroke="#bbb"/>
    <line x1="37" y1="37" x2="31" y2="31" stroke="#aaa"/>
    <line x1="23" y1="43" x2="23" y2="33" stroke="#999"/>
    <line x1="9" y1="37" x2="15" y2="31" stroke="#888"/>
    <line x1="3" y1="23" x2="13" y2="23" stroke="#666"/>
    <line x1="9" y1="9" x2="15" y2="15" stroke="#444"/>
  </g>
</svg>

<footer class="footer">
  <div class="footer-brand"><span class="dot"></span>Hueboard</div>
</footer>

</body>
</html>
```